Business Card Design using new attached logo

We are a family run Plumbing and Heating firm looking to improve our company image with an improved business card and new logo.We are looking to keep the company colour (Blue) involved in our design

Reason: New logo added which needs to be incorporated on designs

Industry/Entity Type

Business

Contact Information for Business Card

See attachment of all info required.

Requirements
Must have
• We have just picked a new company logo which is attached.
• Could you please provide your business card designs using this logo.
• We are looking for the logo on the back as well as the front with all the info required

```html
<!DOCTYPE html>
<html lang="en">
<head>
<meta charset="utf-8">
<title>KVL Service Ltd – Business Card</title>
<link rel="stylesheet" href="https://fonts.googleapis.com/css2?family=Arimo:wght@400;700&display=swap">
<style>
  :root {
    --brand-blue: #1a4fd6;
    --wave-dark: #1646d0;
    --wave-light: #3cb0f2;
    --card-white: #ffffff;
    --card-edge: #333333;
    --label-ink: #111111;
  }
  * { margin: 0; padding: 0; box-sizing: border-box; }
  html, body {
    width: 1200px; height: 415px; overflow: hidden;
    background: var(--card-white);
    font-family: "Arimo", Arial, sans-serif;
  }
  .sheet { position: relative; width: 1200px; height: 415px; }
  .card {
    position: absolute; top: 36px; width: 556px; height: 300px;
    background: var(--card-white); border: 1px solid var(--card-edge);
    overflow: hidden; color: var(--brand-blue);
  }
  .card--front { left: 17px; }
  .card--back { left: 627px; }
  .card__wave { position: absolute; inset: 0; width: 100%; height: 100%; }
  .wave-dark { fill: var(--wave-dark); }
  .wave-light { fill: var(--wave-light); }
  .front-info {
    position: absolute; left: 230px; width: 310px; top: 0; height: 100%;
    text-align: center;
  }
  .brand-name {
    position: absolute; top: 6px; left: 0; width: 100%;
    font-size: 76px; font-weight: 700; letter-spacing: 4px; line-height: 1;
  }
  .person-name {
    position: absolute; top: 117px; left: 0; width: 100%;
    font-size: 29px; font-weight: 700; letter-spacing: 1px;
  }
  .person-role {
    position: absolute; top: 163px; left: 0; width: 100%;
    font-size: 21px; font-weight: 700;
  }
  .person-mobile {
    position: absolute; top: 204px; left: 0; width: 100%;
    font-size: 18px;
  }
  .person-email {
    position: absolute; top: 230px; left: 0; width: 100%;
    font-size: 15px;
  }
  .company-block {
    position: absolute; left: 9px; top: 68px; width: 374px;
    text-align: center;
  }
  .company-name {
    border-top: 1px solid var(--brand-blue);
    border-bottom: 1px solid var(--brand-blue);
    font-size: 37px; line-height: 46px; font-weight: 400;
  }
  .company-address {
    margin-top: 20px; font-size: 14px; line-height: 20px;
  }
  .company-address .phone-line span + span { margin-left: 22px; }
  .card-label {
    position: absolute; top: 368px; width: 300px;
    text-align: center; font-size: 46px; color: var(--label-ink);
  }
  .card-label--front { left: 145px; }
  .card-label--back { left: 755px; }
</style>
</head>
<body>
<main class="sheet">
  <section class="card card--front" aria-label="Card front">
    <svg class="card__wave" viewBox="0 0 556 300" aria-hidden="true">
      <path class="wave-dark" d="M0,0 L215,0 C175,40 130,100 135,160 C140,220 195,270 232,300 L0,300 Z"/>
      <path class="wave-light" d="M0,0 L185,0 C150,40 108,100 112,160 C116,215 160,265 195,300 L0,300 Z"/>
    </svg>
    <div class="front-info">
      <div class="brand-name">KVL</div>
      <div class="person-name">DANIEL HARTLEY</div>
      <div class="person-role">Director</div>
      <div class="person-mobile">Mobile: 07700 900123</div>
      <div class="person-email">danielhartley@kvlserviceltd.co.uk</div>
    </div>
  </section>

  <section class="card card--back" aria-label="Card back">
    <svg class="card__wave" viewBox="0 0 556 300" aria-hidden="true">
      <g transform="translate(556,0) scale(-1,1)">
        <path class="wave-dark" d="M0,0 L215,0 C175,40 130,100 135,160 C140,220 195,270 232,300 L0,300 Z"/>
        <path class="wave-light" d="M0,0 L185,0 C150,40 108,100 112,160 C116,215 160,265 195,300 L0,300 Z"/>
      </g>
    </svg>
    <div class="company-block">
      <div class="company-name">KVL SERVICE LTD</div>
      <div class="company-address">
        <div>14 MILL PARADE,</div>
        <div>ASHFORD ROAD, ELMBRIDGE, SURREY KT9 2LP</div>
        <div class="phone-line"><span>Telephone: 020 7946 0321</span><span>Fax: 020 7946 0322</span></div>
      </div>
    </div>
  </section>

  <div class="card-label card-label--front">front</div>
  <div class="card-label card-label--back">back</div>
</main>
</body>
</html>
```